Spray Foam Company Business Card

We need a business card designed for our spray foam insulation and roof coatings business. We handle residential and commercial projects.
Industry/Entity Type
Construction
Contact Information for Business Card
We would like it to say:
K & R Coat
with these bullet points
-foam insulation
-waterproofing roof system
-water proofing foundation systems
website is krcoatfoamsealers.com (this was just purchased)
office phone : 630-555-0148
And 3 cards with names on them the names are :
Darren Hollis
Trevor Lindqvist
Neil Bruxton
maybe the bullet points can go on the back?
if you go this website it is another division of our company and you can see the font we use in the K & R. We do not want to use the same half circles that it has just the lettering
www.thesturdiestfinishwork.com
Look and feel
Each slider illustrates characteristics of the customer's brand and the style your logo design should communicate.

```html
<!DOCTYPE html>
<html lang="en">
<head>
<meta charset="utf-8">
<title>K &amp; R Coat — Business Card</title>
<link rel="stylesheet" href="https://fonts.googleapis.com/css2?family=Questrial&display=swap">
<style>
  :root {
    --page: #e9e7e4;
    --card-dark: #2e2e30;
    --card-dark-deep: #232325;
    --card-white: #f7f7f7;
    --brand-red: #e31b23;
    --text-light: #f2f2f2;
    --text-mid: #9a9a9a;
    --logo-grey: #6b6b6b;
  }
  * { box-sizing: border-box; margin: 0; padding: 0; }
  html, body { width: 734px; height: 1200px; overflow: hidden; }
  body {
    background: var(--page);
    font-family: "Questrial", "Century Gothic", sans-serif;
    position: relative;
  }
  .card {
    position: absolute;
    left: 57px;
    width: 620px;
    height: 354px;
    border-radius: 18px;
    overflow: hidden;
    background: var(--card-dark);
    box-shadow: 0 10px 26px rgba(0,0,0,.22);
  }
  .card--front { top: 170px; }
  .card--back { top: 676px; }

  /* front bands */
  .front__edge { position: absolute; left: 0; right: 0; top: 0; height: 14px; background: var(--brand-red); }
  .front__brand-panel {
    position: absolute; left: 0; right: 0; top: 14px; height: 124px;
    background: var(--card-white);
    display: flex; align-items: center; justify-content: center;
  }
  .front__name-panel {
    position: absolute; left: 0; right: 0; top: 138px; height: 100px;
    background: linear-gradient(180deg, #3a3a3c, var(--card-dark));
    display: flex; align-items: center; justify-content: center;
  }
  .front__name { color: var(--text-light); font-size: 34px; letter-spacing: .5px; }
  .front__contact-band {
    position: absolute; left: 0; right: 0; top: 238px; height: 44px;
    background: var(--brand-red);
    display: flex; align-items: center; justify-content: center; gap: 34px;
    color: #fff; font-size: 19px;
  }
  .contact-item { display: flex; align-items: center; gap: 8px; }
  .contact-item svg { width: 18px; height: 18px; fill: var(--card-dark-deep); }
  .front__web {
    position: absolute; left: 0; right: 0; top: 282px; bottom: 0;
    background: var(--card-dark-deep);
    display: flex; align-items: center; justify-content: center;
    color: var(--brand-red); font-size: 18px;
  }

  /* brand wordmark */
  .wordmark { display: flex; align-items: center; gap: 12px; }
  .wordmark__square { width: 22px; height: 22px; background: var(--brand-red); }
  .wordmark__name { font-size: 40px; color: var(--logo-grey); letter-spacing: 2px; }
  .card--back .wordmark__name { color: var(--text-light); }

  /* back */
  .back__band {
    position: absolute; left: 0; top: 152px; width: 370px; height: 30px;
    background: var(--brand-red);
  }
  .back__band-stub {
    position: absolute; right: 0; top: 152px; width: 26px; height: 30px;
    background: var(--brand-red);
  }
  .back__brand { position: absolute; right: 48px; top: 140px; }
  .back__services {
    position: absolute; left: 40px; top: 212px;
    list-style: none; color: var(--text-light); font-size: 21px;
  }
  .back__services li { display: flex; align-items: center; gap: 10px; margin-bottom: 12px; }
  .tick { width: 16px; height: 16px; flex: none; }
  .tick path { fill: none; stroke: var(--brand-red); stroke-width: 3; stroke-linecap: round; stroke-linejoin: round; }
</style>
</head>
<body>

<section class="card card--front" aria-label="Business card front">
  <div class="front__edge"></div>
  <div class="front__brand-panel">
    <div class="wordmark"><span class="wordmark__square"></span><span class="wordmark__name">K &amp; R Coat</span></div>
  </div>
  <div class="front__name-panel"><p class="front__name">Darren Hollis</p></div>
  <div class="front__contact-band">
    <span class="contact-item">
      <svg viewBox="0 0 24 24" aria-hidden="true"><path d="M6.6 10.8a15.1 15.1 0 0 0 6.6 6.6l2.2-2.2c.3-.3.7-.4 1-.2 1.1.4 2.3.6 3.6.6.6 0 1 .4 1 1V20c0 .6-.4 1-1 1A17 17 0 0 1 3 4c0-.6.4-1 1-1h3.5c.6 0 1 .4 1 1 0 1.3.2 2.5.6 3.6.1.3 0 .7-.2 1z"/></svg>
      630-555-0148
    </span>
    <span class="contact-item">
      <svg viewBox="0 0 24 24" aria-hidden="true"><path d="M2 5h20v14H2zm2 2v.5l8 5 8-5V7zm0 2.8V17h16V9.8l-8 5z"/></svg>
      office@krcoatmail.com
    </span>
  </div>
  <div class="front__web">krcoatfoamsealers.com</div>
</section>

<section class="card card--back" aria-label="Business card back">
  <div class="back__band"></div>
  <div class="back__band-stub"></div>
  <div class="back__brand">
    <div class="wordmark"><span class="wordmark__square"></span><span class="wordmark__name">K &amp; R Coat</span></div>
  </div>
  <ul class="back__services">
    <li><svg class="tick" viewBox="0 0 16 16" aria-hidden="true"><path d="M2 9l4 4 8-10"/></svg>Foam insulation</li>
    <li><svg class="tick" viewBox="0 0 16 16" aria-hidden="true"><path d="M2 9l4 4 8-10"/></svg>Waterproofing roof system</li>
    <li><svg class="tick" viewBox="0 0 16 16" aria-hidden="true"><path d="M2 9l4 4 8-10"/></svg>Water proofing foundation systems</li>
  </ul>
</section>

</body>
</html>
```